Kelvo Commercial Cleaning is lookong for a new business card design.

A fresh new design that's professional and stylish. We need a serious upgrade to our business cards. I have included pictures of our existing ones. Our clients include professional individuals and business owners. We woupdblike something professional and upbeat. Please have fun and see what you come uo with.

Target Market(s)

Property managers, business owners, facility managers and other similar professionals

Industry/Entity Type

Janitorial

Contact Information for Business Card

Name, cell, office number, email, web address

Font styles to use
Sans Serif

Colors

Designer to choose colors to be used in the design.

Requirements
Must have
• please use the green color in our logo
Nice to have
• Bar code
Should not have
• Address

```html
<!DOCTYPE html>
<html lang="en">
<head>
<meta charset="utf-8">
<title>Kelvo Commercial Cleaning – Business Card</title>
<link rel="stylesheet" href="https://fonts.googleapis.com/css2?family=Figtree:wght@400;500;700&display=swap">
<style>
  :root {
    --bg: #e4e3e1;
    --blue-dark: #2c5d94;
    --blue-light: #4a7fb0;
    --blue-text: #2a5790;
    --green: #35ab4f;
    --white: #f6f6f4;
    --card-white: #f4f4f4;
    --card-white-2: #e9e9e9;
    --grey-text: #5a5a5e;
  }
  * { margin: 0; padding: 0; box-sizing: border-box; }
  html, body {
    width: 1200px; height: 1200px; overflow: hidden;
    background: var(--bg);
    font-family: "Figtree", "Helvetica Neue", Arial, sans-serif;
  }
  .canvas { position: relative; width: 1200px; height: 1200px; }
  .card {
    position: absolute; left: 226px; width: 706px; height: 403px;
  }
  .card--front {
    top: 155px;
    background: linear-gradient(120deg, var(--blue-dark) 0%, var(--blue-light) 100%);
    color: var(--white);
    text-align: center;
  }
  .brand-block { position: absolute; left: 0; right: 0; top: 112px; }
  .brand-name {
    font-size: 118px; font-weight: 700; line-height: 1; letter-spacing: -1px;
  }
  .brand-sub {
    margin-top: 12px; font-size: 23px; font-weight: 700; letter-spacing: 0.5px; line-height: 1.2;
  }
  .tagline {
    position: absolute; left: 0; right: 0; top: 349px;
    font-size: 18px; font-weight: 400; letter-spacing: 0.6px; line-height: 1.2;
  }
  .card--back {
    top: 610px;
    background: linear-gradient(120deg, var(--card-white) 0%, var(--card-white-2) 60%, var(--card-white) 100%);
  }
  .back-brand {
    position: absolute; right: 47px; top: 42px;
    font-size: 100px; font-weight: 700; line-height: 1; letter-spacing: -1px;
    color: var(--green);
  }
  .person-name {
    position: absolute; left: 47px; top: 203px;
    font-size: 29px; font-weight: 700; line-height: 1.2; color: var(--blue-text);
  }
  .contact-list {
    position: absolute; left: 47px; top: 276px; list-style: none;
  }
  .contact-item {
    display: flex; align-items: center; gap: 10px;
    height: 27px; font-size: 19px; color: var(--grey-text);
  }
  .contact-icon { width: 15px; height: 15px; fill: var(--blue-text); flex: none; }
</style>
</head>
<body>
<main class="canvas">
  <section class="card card--front">
    <div class="brand-block">
      <div class="brand-name">kelvo</div>
      <div class="brand-sub">commercial cleaning</div>
    </div>
    <p class="tagline">clean spaces, clear minds</p>
  </section>

  <section class="card card--back">
    <div class="back-brand">kelvo</div>
    <h1 class="person-name">Dana Whitfield</h1>
    <ul class="contact-list">
      <li class="contact-item">
        <svg class="contact-icon" viewBox="0 0 24 24" aria-hidden="true"><path d="M6.6 10.8a15.1 15.1 0 0 0 6.6 6.6l2.2-2.2a1 1 0 0 1 1-.25 11.4 11.4 0 0 0 3.6.57 1 1 0 0 1 1 1V20a1 1 0 0 1-1 1A17 17 0 0 1 3 4a1 1 0 0 1 1-1h3.5a1 1 0 0 1 1 1c0 1.25.2 2.45.57 3.57a1 1 0 0 1-.25 1z"/></svg>
        (555) 014-2287
      </li>
      <li class="contact-item">
        <svg class="contact-icon" viewBox="0 0 24 24" aria-hidden="true"><path d="M2 5h20v14H2z"/><path d="M3 6.2l9 7.1 9-7.1" fill="none" stroke="#fff" stroke-width="1.6" opacity="0.8"/></svg>
        dana@kelvocleaning.com
      </li>
      <li class="contact-item">
        <svg class="contact-icon" viewBox="0 0 24 24" aria-hidden="true"><path d="M12 2a10 10 0 1 0 0 20 10 10 0 0 0 0-20zm6.9 6h-3a15.7 15.7 0 0 0-1.3-3.6A8 8 0 0 1 18.9 8zM12 4c.8 1.2 1.5 2.5 1.9 4h-3.8c.4-1.5 1.1-2.8 1.9-4zM4.3 14a8 8 0 0 1 0-4h3.4a16 16 0 0 0 0 4zm.8 2h3a15.7 15.7 0 0 0 1.3 3.6A8 8 0 0 1 5.1 16zm3-8h-3a8 8 0 0 1 4.3-3.6A15.7 15.7 0 0 0 8.1 8zM12 20c-.8-1.2-1.5-2.5-1.9-4h3.8c-.4 1.5-1.1 2.8-1.9 4zm2.3-6H9.7a14.5 14.5 0 0 1 0-4h4.6a14.5 14.5 0 0 1 0 4zm.3 5.6a15.7 15.7 0 0 0 1.3-3.6h3a8 8 0 0 1-4.3 3.6zm1.7-5.6a16 16 0 0 0 0-4h3.4a8 8 0 0 1 0 4z"/></svg>
        www.kelvocleaning.com
      </li>
    </ul>
  </section>
</main>
</body>
</html>
```